Business Card Design

We need a business card design for a new company called Riverbend Advisory, LLC. We are a project management and software engineering consulting company. We prefer to use blues but am open to any colors. We would like out design to show strength and creativity.

I've uploaded new logo designs to the project.  Please use these logo designs for the business card. Thanks!

Industry/Entity Type

Software

Contact Information for Business Card

Daniel Whitford
Consultant
Owner

Riverbend Advisory, LLC

2716 5th St. S #4372
Arlington, VA 22198

703-555-0187
dwhitford@rvbadv.example
www.rvbadv.example

```html
<!DOCTYPE html>
<html lang="en">
<head>
<meta charset="utf-8">
<title>Riverbend Advisory – Business Card</title>
<link rel="stylesheet" href="https://fonts.googleapis.com/css2?family=Rubik:ital,wght@0,400;0,500;0,700;1,700&display=swap">
<style>
  :root {
    --navy: #0d3a63;
    --red: #c8332c;
    --paper: #ffffff;
    --backdrop: #3b3b3d;
    --rule: #1f4a73;
  }
  * { box-sizing: border-box; margin: 0; padding: 0; }
  html, body { width: 1200px; height: 900px; overflow: hidden; }
  body {
    background: var(--backdrop);
    font-family: "Rubik", Arial, sans-serif;
    display: flex;
    flex-direction: column;
    align-items: center;
    justify-content: center;
    gap: 50px;
  }
  .card {
    position: relative;
    width: 630px;
    height: 360px;
    background: var(--paper);
    overflow: hidden;
  }

  /* Front */
  .card-front .wordmark {
    position: absolute;
    top: 118px;
    left: 0; right: 0;
    text-align: center;
    color: var(--navy);
    font-weight: 500;
    font-size: 46px;
    letter-spacing: -0.5px;
    line-height: 1;
  }
  .card-front .band {
    position: absolute;
    left: 0; right: 0;
    top: 228px;
    height: 64px;
    background: var(--navy);
    display: flex;
    align-items: center;
    justify-content: center;
    color: var(--paper);
    font-size: 24px;
    letter-spacing: 0.3px;
  }

  /* Back */
  .card-back .wordmark {
    position: absolute;
    top: 62px;
    left: 52px;
    color: var(--navy);
    font-weight: 500;
    font-size: 27px;
    letter-spacing: -0.3px;
  }
  .card-back .divider {
    position: absolute;
    left: 352px;
    top: 54px;
    width: 1.5px;
    height: 54px;
    background: var(--rule);
  }
  .card-back .tagline {
    position: absolute;
    left: 372px;
    top: 60px;
    color: var(--red);
    font-weight: 700;
    font-size: 11px;
    letter-spacing: 2.4px;
    line-height: 1.55;
    text-transform: uppercase;
  }
  .card-back .person {
    position: absolute;
    left: 70px;
    top: 138px;
  }
  .person .name {
    color: var(--navy);
    font-weight: 700;
    font-style: italic;
    font-size: 25px;
  }
  .person .role {
    color: var(--red);
    font-size: 16px;
    margin-top: 4px;
  }
  .contact-list {
    position: absolute;
    left: 330px;
    top: 150px;
    list-style: none;
    color: var(--navy);
    font-size: 15px;
  }
  .contact-list li {
    display: flex;
    align-items: flex-start;
    gap: 14px;
    margin-bottom: 9px;
    line-height: 1.35;
  }
  .contact-list .icon {
    flex: 0 0 24px;
    width: 24px;
    height: 24px;
  }
  .contact-list span { padding-top: 2px; }
</style>
</head>
<body>

  <section class="card card-front" aria-label="Business card front">
    <div class="wordmark">Riverbend Advisory</div>
    <div class="band">www.rvbadv.example</div>
  </section>

  <section class="card card-back" aria-label="Business card back">
    <div class="wordmark">Riverbend Advisory</div>
    <div class="divider"></div>
    <p class="tagline">Project management and<br>software engineering consulting</p>

    <div class="person">
      <p class="name">Daniel Whitford</p>
      <p class="role">Consultant Owner</p>
    </div>

    <ul class="contact-list">
      <li>
        <svg class="icon" viewBox="0 0 24 24" fill="none" stroke="var(--navy)" stroke-width="1.4">
          <circle cx="12" cy="12" r="11"/>
          <rect x="8.5" y="5.5" width="7" height="13" rx="1.2"/>
          <line x1="10.5" y1="16" x2="13.5" y2="16"/>
        </svg>
        <span>703-555-0187</span>
      </li>
      <li>
        <svg class="icon" viewBox="0 0 24 24" fill="none" stroke="var(--navy)" stroke-width="1.4">
          <circle cx="12" cy="12" r="11"/>
          <ellipse cx="12" cy="12" rx="4" ry="8"/>
          <line x1="4" y1="12" x2="20" y2="12"/>
          <line x1="5.5" y1="8" x2="18.5" y2="8"/>
          <line x1="5.5" y1="16" x2="18.5" y2="16"/>
        </svg>
        <span>www.rvbadv.example</span>
      </li>
      <li>
        <svg class="icon" viewBox="0 0 24 24" fill="none" stroke="var(--navy)" stroke-width="1.4">
          <circle cx="12" cy="12" r="11"/>
          <rect x="6" y="8" width="12" height="8.5" rx="0.8"/>
          <polyline points="6,8 12,13 18,8"/>
        </svg>
        <span>dwhitford@rvbadv.example</span>
      </li>
      <li>
        <svg class="icon" viewBox="0 0 24 24" fill="none" stroke="var(--navy)" stroke-width="1.4">
          <circle cx="12" cy="12" r="11"/>
          <path d="M12 19 C9 15 7.5 12.5 7.5 10.5 A4.5 4.5 0 0 1 16.5 10.5 C16.5 12.5 15 15 12 19 Z"/>
          <circle cx="12" cy="10.5" r="1.6"/>
        </svg>
        <span>2716 5th St. S #4372<br>Arlington, VA 22198</span>
      </li>
    </ul>
  </section>

</body>
</html>
```